Homecare Design. I would like the color to be same as my business cards

Gentle Hearthkeeper & Helper Agency
I would something very light on the eyes.
Easy to read nothing complicated
I want something that demonstrate soft touch

My contact number has change cell: 203-555-0187 office: 2035550142

Target Market(s)

Elderly
people looking for someone to take care of there love ones
Target age starting at 50

Industry/Entity Type

Business

Font styles to use
Serif

Colors
3176b5
3276b5
85acd3
ceddec

Requirements
Must have

Nice to have
• I woluld like something like helping hands
Should not have
• I really don't care to see medical supplies, medication

```html
<!DOCTYPE html>
<html lang="en">
<head>
<meta charset="utf-8">
<title>Gentle Hearthkeeper &amp; Helper Agency – Postcard</title>
<link href="https://fonts.googleapis.com/css2?family=Tinos:wght@400;700&display=swap" rel="stylesheet">
<style>
  :root {
    --blue-deep: #3176b5;
    --blue-text: #3276b5;
    --blue-mid: #85acd3;
    --blue-pale: #ceddec;
    --white: #ffffff;
    --backdrop: #eef0f2;
    --line: #d3dfec;
    --skin: #e9b8a0;
    --sleeve: #f7eef2;
  }
  * { box-sizing: border-box; margin: 0; padding: 0; }
  html, body { width: 957px; height: 1200px; overflow: hidden; }
  body {
    background: var(--backdrop);
    font-family: "Tinos", "Times New Roman", serif;
    color: var(--blue-text);
    position: relative;
  }
  .card {
    position: absolute;
    width: 672px;
    background: var(--white);
    border: 1px solid #e2e6ea;
  }
  /* Front */
  .card--front { left: 74px; top: 78px; height: 519px; }
  .front__band {
    position: absolute; left: 0; top: 16px; width: 100%; height: 54px;
    background: var(--blue-mid);
    color: var(--white);
    font-size: 29px; line-height: 54px; text-align: center;
  }
  .front__photo {
    position: absolute; left: 0; top: 70px; width: 100%; height: 333px;
    background: linear-gradient(100deg, var(--sleeve) 0%, var(--white) 22%, var(--skin) 45%, #e3a98f 70%, var(--white) 92%);
  }
  .front__tagline {
    position: absolute; right: 26px; top: 358px;
    font-size: 22px; color: var(--blue-deep);
  }
  .front__about {
    position: absolute; left: 0; top: 403px; width: 100%; height: 116px;
    background: var(--blue-pale);
    padding: 13px 18px 0;
    font-size: 15px; line-height: 20px; text-align: center;
  }
  .front__about strong { font-weight: 700; }
  /* Back */
  .card--back { left: 187px; top: 639px; height: 520px; }
  .back__panel {
    position: absolute; left: 0; top: 0; width: 359px; height: 434px;
    background: var(--blue-pale);
    overflow: hidden;
  }
  .back__band {
    position: absolute; left: 0; top: 30px; width: 100%; height: 29px;
    background: var(--blue-mid); color: var(--white);
    font-size: 14.5px; line-height: 29px; text-align: center;
  }
  .back__hands {
    position: absolute; left: 0; top: 190px; width: 100%; height: 150px;
    background: linear-gradient(160deg, transparent 10%, rgba(133,172,211,0.55) 40%, rgba(133,172,211,0.55) 60%, transparent 90%);
  }
  .contact { position: absolute; left: 27px; top: 86px; font-size: 13.5px; line-height: 20px; }
  .contact__title { font-weight: 700; margin-bottom: 4px; }
  .contact__phone { margin-top: 6px; }
  .hours {
    position: absolute; left: 0; top: 217px; width: 100%;
    text-align: center; font-size: 13.5px; line-height: 18px;
  }
  .website {
    position: absolute; left: 0; top: 387px; width: 100%;
    text-align: center; font-size: 19px;
  }
  .stamp {
    position: absolute; left: 558px; top: 33px; width: 83px; height: 78px;
    border: 1.5px solid var(--line);
  }
  .address-line {
    position: absolute; left: 429px; width: 213px; height: 0;
    border-top: 1.5px solid var(--line);
  }
</style>
</head>
<body>
  <section class="card card--front">
    <div class="front__band">Gentle Hearthkeeper &amp; Helper Agency</div>
    <div class="front__photo" role="img" aria-label="Photo of a caregiver's hands gently holding an elderly person's hand"></div>
    <div class="front__tagline">Helping Hands</div>
    <p class="front__about"><strong>Gentle Hearthkeeper &amp; Helper Agency</strong>, assist elderly clients who need assistance<br>in or out of the home. Our home care services to our clients to assist them to lead dignified<br>and independent lives in the comfort and safety of there own homes. We provide personalized,<br>high-quality care on an as-needed or preventative basis.</p>
  </section>

  <section class="card card--back">
    <div class="back__panel">
      <div class="back__band">Gentle Hearthkeeper &amp; Helper Agency</div>
      <div class="back__hands" role="img" aria-label="Faint illustration of two hands reaching toward each other"></div>
      <div class="contact">
        <p class="contact__title">Contact us:</p>
        <p>Address: 48 LINDEN ST FAIRHAVEN CT 06512</p>
        <p>info@gentlehearthkeeperhelper.com</p>
        <p class="contact__phone">Phone: 203-555-0187 | 203-555-0142</p>
      </div>
      <div class="hours">
        <p>Office Hours</p>
        <p>Monday - Friday: 8:00 - 5:00 pm.</p>
        <p>Saturday: 8:00 - 2:00 pm.</p>
        <p>Sunday: Closed</p>
      </div>
      <p class="website">gentlehearthkeeperhelper.com</p>
    </div>
    <div class="stamp"></div>
    <div class="address-line" style="top:182px"></div>
    <div class="address-line" style="top:217px"></div>
    <div class="address-line" style="top:251px"></div>
    <div class="address-line" style="top:286px"></div>
  </section>
</body>
</html>
```